Name Card, Stationary, Warranty Seal, Receipt Book
Qorvix Repair Centre
Simple
Tomas
27 Wexley Lane #08-04
Singapore 58817
qrv@qorvix-mail.test
www.qorvix-fix.test
State in we Repair veltra, Plumstone, Korvane and others Smart Phones
On the spot Repair.
For this you are able to use your creative base on our line of repair service

```html
<!DOCTYPE html>
<html lang="en">
<head>
<meta charset="utf-8">
<title>Qorvix Repair Centre – Stationery Set</title>
<link href="https://fonts.googleapis.com/css2?family=Exo+2:wght@400;700;800&display=swap" rel="stylesheet">
<style>
:root{
  --board:#3b3b3d;
  --paper:#ffffff;
  --orange:#f26522;
  --red:#e3251f;
  --blue:#1d5fc2;
  --ink:#555a60;
  --rule:#f6a86f;
  --faint:#fde3d2;
}
*{margin:0;padding:0;box-sizing:border-box}
html,body{width:1200px;height:281px;overflow:hidden;background:var(--board);font-family:"Exo 2",sans-serif;color:var(--ink)}
.board{position:relative;width:1200px;height:281px}
.piece{position:absolute;background:var(--paper);box-shadow:0 2px 5px rgba(0,0,0,.45)}
.brand{display:flex;align-items:center;gap:4px;font-weight:800;color:var(--orange);line-height:1}
.brand .dot{border-radius:50%;background:var(--orange);flex:none}
.tag{font-weight:700;letter-spacing:.12em;color:var(--ink);text-transform:uppercase}

/* master logo */
.master{position:absolute;left:14px;top:14px}
.master .brand{font-size:36px;gap:8px}
.master .brand .dot{width:26px;height:26px}
.master .tag{font-size:10px;color:#ddd;margin:4px 0 0 34px}

/* seal */
.seal{position:absolute;left:16px;top:160px;width:78px;height:78px;border-radius:50%;background:#d9dadc;border:4px dashed #f0f0f0;display:flex;align-items:center;justify-content:center;flex-direction:column;text-align:center}
.seal .inner{width:54px;height:54px;border-radius:50%;background:var(--paper);display:flex;flex-direction:column;align-items:center;justify-content:center;font-size:6px;font-weight:700;color:var(--red);line-height:1.1}
.seal .dot{width:14px;height:14px;border-radius:50%;background:var(--orange);margin-bottom:2px}

/* cards */
.card{width:84px;height:48px;padding:5px;font-size:4px;line-height:1.35}
.card .brand{font-size:11px}
.card .brand .dot{width:8px;height:8px}
.card.blue{background:var(--blue)}
.card.red{background:var(--red)}
.card.blue .brand,.card.red .brand{color:#fff}
.card.blue .brand .dot,.card.red .brand .dot{background:#fff}
.card.center{display:flex;align-items:center;justify-content:center}
.card .band{position:absolute;left:0;right:0;bottom:0;height:4px;background:linear-gradient(90deg,var(--red),var(--orange))}

/* letterhead */
.letter{left:300px;top:10px;width:166px;height:262px;padding:10px;overflow:hidden}
.letter .brand{font-size:14px}
.letter .brand .dot{width:11px;height:11px}
.contact{position:absolute;right:10px;top:10px;font-size:4px;line-height:1.4;text-align:right}
.watermark{position:absolute;left:18px;top:36px;width:56px;height:56px;border-radius:50%;background:var(--faint)}
.footband{position:absolute;left:0;right:0;bottom:0;height:6px;background:linear-gradient(90deg,var(--red),var(--orange))}

/* receipt */
.receipt{left:478px;top:10px;width:166px;height:262px;padding:10px}
.receipt .brand{font-size:14px}
.receipt .brand .dot{width:11px;height:11px}
.receipt h2{position:absolute;right:10px;top:12px;font-size:9px;color:var(--orange);font-weight:800;text-transform:uppercase}
.items{position:absolute;left:10px;right:10px;top:52px;height:160px;border:1px solid var(--rule);background:repeating-linear-gradient(#fff 0 7px,var(--faint) 7px 8px)}
.items .head{display:grid;grid-template-columns:14% 48% 19% 19%;background:var(--orange);color:#fff;font-size:4.5px;font-weight:700;height:9px;align-items:center;text-align:center}
.items .cols{position:absolute;top:9px;bottom:0;left:0;right:0;display:grid;grid-template-columns:14% 48% 19% 19%}
.items .cols span{border-right:1px solid var(--rule)}
.items .cols span:last-child{border:0}
.total{position:absolute;right:10px;top:216px;font-size:5px;font-weight:700;width:60px;border:1px solid var(--rule);padding:2px 4px}
.sign{position:absolute;left:10px;top:240px;width:70px;border-top:1px solid var(--ink);font-size:4px;padding-top:2px}

/* compliment slips */
.slip{width:146px;height:76px;padding:8px}
.slip .brand{font-size:12px}
.slip .brand .dot{width:9px;height:9px}

/* envelopes */
.env{position:absolute;width:260px;height:110px;box-shadow:0 2px 6px rgba(0,0,0,.5)}
.env svg{position:absolute;inset:0}
.env .brand{position:absolute;left:12px;top:10px;font-size:14px}
.env .brand .dot{width:11px;height:11px}
</style>
</head>
<body>
<main class="board">

  <header class="master">
    <div class="brand"><span class="dot"></span>Qorvix</div>
    <div class="tag">Repair Centre</div>
  </header>

  <div class="seal" aria-label="Warranty seal">
    <div class="inner"><span class="dot"></span>WARRANTY<br>VOID IF<br>REMOVED</div>
  </div>

  <!-- business cards -->
  <section class="piece card" style="left:110px;top:160px">
    <div class="brand"><span class="dot"></span>Qorvix</div>
    <p style="margin-top:4px"><b>Tomas</b><br>qrv@qorvix-mail.test<br>www.qorvix-fix.test</p>
    <div class="band"></div>
  </section>
  <section class="piece card" style="left:200px;top:160px">
    <p style="margin-top:8px">27 Wexley Lane #08-04<br>Singapore 58817<br>On the spot Repair.</p>
    <div class="band"></div>
  </section>
  <section class="piece card blue center" style="left:14px;top:222px">
    <div class="brand"><span class="dot"></span>Qorvix</div>
  </section>
  <section class="piece card center" style="left:106px;top:222px">
    <div class="brand"><span class="dot"></span>Qorvix</div>
  </section>
  <section class="piece card red center" style="left:196px;top:222px">
    <div class="brand"><span class="dot"></span>Qorvix</div>
  </section>

  <!-- letterhead -->
  <section class="piece letter">
    <div class="brand"><span class="dot"></span>Qorvix</div>
    <div class="contact">27 Wexley Lane #08-04<br>Singapore 58817<br>qrv@qorvix-mail.test<br>www.qorvix-fix.test</div>
    <div class="watermark"></div>
    <div class="footband"></div>
  </section>

  <!-- receipt -->
  <section class="piece receipt">
    <div class="brand"><span class="dot"></span>Qorvix</div>
    <h2>Invoice</h2>
    <div class="items">
      <div class="head"><span>Qty</span><span>Description</span><span>Price</span><span>Amount</span></div>
      <div class="cols"><span></span><span></span><span></span><span></span></div>
    </div>
    <div class="total">Total</div>
    <div class="sign">Customer Signature</div>
  </section>

  <!-- compliment slips -->
  <section class="piece slip" style="left:672px;top:104px">
    <div class="brand"><span class="dot"></span>Qorvix</div>
    <div class="footband" style="height:4px"></div>
  </section>
  <section class="piece slip" style="left:672px;top:196px">
    <div class="brand"><span class="dot"></span>Qorvix</div>
    <div class="footband" style="height:4px"></div>
  </section>

  <!-- envelopes -->
  <section class="env" style="left:930px;top:80px;background:var(--blue)">
    <svg viewBox="0 0 260 110" preserveAspectRatio="none"><path d="M0 0 L130 62 L260 0" fill="none" stroke="#174f9f" stroke-width="2"/></svg>
  </section>
  <section class="env" style="left:930px;top:128px;background:var(--red)">
    <svg viewBox="0 0 260 110" preserveAspectRatio="none"><path d="M0 0 L130 66 L260 0 Z" fill="#c81e19"/></svg>
    <div class="brand" style="left:118px;top:26px;color:#fff"><span class="dot" style="background:#fff"></span></div>
  </section>
  <section class="env" style="left:930px;top:186px;background:var(--paper);height:92px">
    <svg viewBox="0 0 260 92" preserveAspectRatio="none"><path d="M0 0 L130 56 L260 0" fill="none" stroke="#d5d5d5" stroke-width="1.5"/></svg>
    <div class="brand"><span class="dot"></span>Qorvix</div>
  </section>

</main>
</body>
</html>
```